Willowmere Accord Business Card

Need a business card for my nonprofit, Willowmere Accord Inc. Willowmere Accord is a conflict resolution practice that offers services that help people resolve problems peacefully.

Got Conflict? Try Conflict Coaching. Initial consultation is complimentary

Marissa Dovrell-Kantz, PhD
Willowmere Accord Inc.
www.willowmereaccord.org
E: info@willowmereaccord.org
P: 555-318-4702

Would like the attached logo on it, as well as our slogan, which is Bringing Peace to the TableĀ®

```html
<!DOCTYPE html>
<html lang="en">
<head>
<meta charset="utf-8">
<title>Willowmere Accord Business Card</title>
<link rel="stylesheet" href="https://fonts.googleapis.com/css2?family=Roboto+Condensed:wght@300;400&display=swap">
<style>
  :root{
    --page:#ffffff;
    --board:#211c1a;
    --card:#ffffff;
    --gold:#dcb954;
    --gold-deep:#b8962e;
    --red:#e0434a;
    --white:#ffffff;
  }
  *{margin:0;padding:0;box-sizing:border-box}
  html,body{width:1200px;height:1200px;overflow:hidden;background:var(--page)}
  body{position:relative;font-family:"Roboto Condensed",Arial,sans-serif}
  .board{position:absolute;left:125px;top:64px;width:929px;height:1070px;background:var(--board)}
  .card{position:absolute;left:240px;width:700px;height:400px;background:var(--card);overflow:hidden}
  .card--front{top:192px}
  .card--back{top:606px}

  .brand{position:absolute;display:flex;align-items:center;color:var(--gold-deep);font-weight:400;line-height:.95;text-transform:uppercase;letter-spacing:1px}
  .brand__dot{border-radius:50%;background:var(--red);flex:none}
  .card--front .brand{left:0;right:0;top:112px;justify-content:center;gap:22px;font-size:58px}
  .card--front .brand__dot{width:64px;height:64px}
  .card--back .brand{left:40px;top:66px;gap:14px;font-size:40px}
  .card--back .brand__dot{width:42px;height:42px}

  .name-band{position:absolute;left:0;right:0;top:338px;height:50px;background:var(--gold);color:var(--white);
    font-weight:300;font-size:38px;text-align:center;line-height:50px;letter-spacing:.2px}

  .role{position:absolute;left:424px;width:244px;top:30px;text-align:center;color:var(--red);font-size:20px;font-weight:300;
    padding-bottom:4px;border-bottom:1px solid var(--red)}
  .person{position:absolute;right:10px;top:66px;color:var(--gold);font-size:22px;font-weight:300}

  .wave{position:absolute;left:0;top:0;width:700px;height:400px}
  .divider{position:absolute;left:361px;top:219px;width:2px;height:159px;background:var(--white)}
  .contact{position:absolute;left:378px;top:244px;list-style:none;color:var(--white);font-size:23px;font-weight:300}
  .contact li{display:flex;align-items:center;gap:12px;height:30px}
  .contact .org{padding-left:30px}
  .contact svg{width:20px;height:20px;flex:none}
</style>
</head>
<body>
  <div class="board"></div>

  <section class="card card--front">
    <div class="brand"><span class="brand__dot"></span><span>Willowmere<br>Accord</span></div>
    <div class="name-band">WILLOWMERE ACCORD INC.</div>
  </section>

  <section class="card card--back">
    <svg class="wave" viewBox="0 0 700 400" aria-hidden="true">
      <path d="M0,220 C60,250 120,262 180,254 C320,236 500,108 700,112 L700,400 L0,400Z" fill="var(--red)"/>
      <path d="M0,223 C60,253 120,264 180,257 C320,240 500,116 700,120 L700,400 L0,400Z" fill="var(--white)"/>
      <path d="M0,226 C60,256 120,266 180,259 C320,244 500,124 700,128 L700,400 L0,400Z" fill="var(--gold)"/>
    </svg>

    <div class="brand"><span class="brand__dot"></span><span>Willowmere<br>Accord</span></div>
    <div class="role">Directer</div>
    <div class="person">Marissa Dovrell-Kantz, PhD</div>

    <div class="divider"></div>
    <ul class="contact">
      <li class="org">Willowmere Accord Inc.</li>
      <li>
        <svg viewBox="0 0 20 20" aria-hidden="true"><circle cx="10" cy="10" r="10" fill="#fff"/><g fill="none" stroke="var(--gold)" stroke-width="1"><circle cx="10" cy="10" r="6"/><ellipse cx="10" cy="10" rx="2.6" ry="6"/><path d="M4 10h12M5 7h10M5 13h10"/></g></svg>
        www.willowmereaccord.org
      </li>
      <li>
        <svg viewBox="0 0 20 20" aria-hidden="true"><circle cx="10" cy="10" r="10" fill="#fff"/><rect x="5" y="6.5" width="10" height="7" fill="none" stroke="var(--gold)" stroke-width="1.2"/><path d="M5 6.5l5 4 5-4" fill="none" stroke="var(--gold)" stroke-width="1.2"/></svg>
        info@willowmereaccord.org
      </li>
      <li>
        <svg viewBox="0 0 20 20" aria-hidden="true"><circle cx="10" cy="10" r="10" fill="#fff"/><path d="M7 5c-1 .6-2 1.6-1.4 3.6.8 2.6 3 5 5.6 6 1.6.6 2.6-.2 3.2-1.2l-2.2-1.8-1.2 1c-1.4-.6-2.6-2-3.2-3.4l1-1.2z" fill="var(--gold)"/></svg>
        555-318-4702
      </li>
    </ul>
  </section>
</body>
</html>
```